you will use Ai to Copy the website Quellabyx.com to come up with the basic frame work and it will give you the understanding of how I would like Zandoprik.com to be like. Zandoprik.com is a peer to peer rv rental site very similar to both of the other rv rental sites the difference is that are commission based 20% and above per rental and we will be one flat monthly rate and they keep all the earnings. Below is photo that will help you with the color scheme and the look and feel of the design

```html
<!DOCTYPE html>
<html lang="en">
<head>
<meta charset="utf-8">
<title>Zandoprik.com — List it. Rent it. Bank it.</title>
<link href="https://fonts.googleapis.com/css2?family=Inter+Tight:wght@600;700;800&family=Inter:wght@400;500;600;700&display=swap" rel="stylesheet">
<style>
:root{
  --navy:#10213f;
  --navy-deep:#07111f;
  --ink:#0e1a2c;
  --muted:#5d6676;
  --green:#7cc242;
  --green-dark:#4d8a23;
  --green-ink:#2f5d16;
  --cream:#f8f8f2;
  --sage:#eef3e3;
  --white:#ffffff;
  --line:#e4e6e0;
  --orange:#f0a03a;
  --heart:#e0303a;
}
*{box-sizing:border-box;margin:0;padding:0}
html,body{width:1200px;height:3815px;overflow:hidden}
body{position:relative;background:var(--cream);font-family:"Inter",sans-serif;color:var(--ink)}
.display{font-family:"Inter Tight",sans-serif;font-weight:700;letter-spacing:-0.055em}
.abs{position:absolute}
.btn{display:inline-flex;align-items:center;justify-content:center;border-radius:999px;font-weight:600;font-size:14px;height:38px;padding:0 16px;text-decoration:none}
.btn-green{background:var(--green);color:var(--navy-deep)}
.btn-white{background:var(--white);color:var(--ink)}
.eyebrow{font-size:11px;font-weight:700;letter-spacing:.14em;text-transform:uppercase;color:var(--green-ink)}

/* hero */
.hero{top:0;left:0;width:1200px;height:720px;background:
  radial-gradient(circle at 760px 140px,#f2a13a 0,#e58a2c 70px,rgba(229,138,44,.25) 150px,transparent 240px),
  radial-gradient(ellipse at 300px 560px,rgba(70,120,90,.55),transparent 420px),
  radial-gradient(ellipse at 950px 620px,rgba(60,110,60,.5),transparent 380px),
  linear-gradient(180deg,#163256 0%,#112746 55%,#0a172b 100%)}
.nav{top:15px;left:74px;width:1037px;height:56px;background:rgba(245,246,244,.95);border-radius:20px;display:flex;align-items:center;padding:0 12px 0 18px}
.brand{display:flex;align-items:center;gap:10px;font-family:"Inter Tight",sans-serif;font-weight:700;font-size:20px;letter-spacing:-0.03em;color:var(--ink)}
.brand-mark{width:34px;height:34px;border-radius:9px;background:var(--navy)}
.nav-links{display:flex;gap:28px;margin-left:100px;font-size:13px;font-weight:500;color:#27324a}
.nav-right{margin-left:auto;display:flex;gap:10px}
.nav-right .btn{height:38px;font-size:13px}
.pill-badge{top:123px;left:75px;height:26px;padding:0 12px;border-radius:999px;background:rgba(255,255,255,.14);border:1px solid rgba(255,255,255,.25);color:#fff;font-size:12px;font-weight:600;display:flex;align-items:center;gap:8px}
.pill-badge i{width:7px;height:7px;border-radius:50%;background:var(--green)}
.hero-title{top:166px;left:74px;font-size:84px;line-height:.9;color:#fff}
.hero-title span{color:var(--green);display:block}
.hero-copy{top:334px;left:75px;width:540px;font-size:19px;line-height:30px;letter-spacing:-0.01em;color:#eef2f7}
.hero-cta{top:478px;left:75px;display:flex;gap:12px}
.hero-cta .btn{height:38px}
.btn-ghost{background:rgba(8,20,38,.55);color:#fff}
.checks{left:75px;display:flex;gap:12px}
.check{height:27px;padding:0 12px;border-radius:999px;background:rgba(8,20,38,.55);border:1px solid rgba(255,255,255,.2);color:#fff;font-size:13px;font-weight:600;display:flex;align-items:center;gap:6px}
.check svg{width:12px;height:12px}
.keep-card{top:185px;left:633px;width:187px;height:111px;background:#fff;border-radius:14px;padding:14px 16px}
.keep-card strong{font-family:"Inter Tight",sans-serif;font-size:28px;letter-spacing:-0.04em;display:block;line-height:1}
.keep-card p{font-size:11px;line-height:13px;color:var(--muted);margin-top:6px}
.hero-art{top:321px;left:622px;width:482px;height:261px;border-radius:22px;border:1px solid rgba(255,255,255,.25);background:linear-gradient(160deg,rgba(255,255,255,.18),rgba(255,255,255,.04)),linear-gradient(180deg,#2b4a6d,#1c3553)}

/* search */
.search{top:659px;left:81px;width:1037px;height:144px;background:#fff;border-radius:22px;box-shadow:0 18px 40px rgba(10,20,40,.12);padding:16px 15px}
.tabs{display:flex;gap:8px}
.tab{height:38px;padding:0 14px;border-radius:999px;border:2px solid #c9ccd1;font-size:12px;font-weight:700;display:flex;align-items:center;color:#333c4b}
.tab.on{background:var(--navy);color:#fff;border-color:var(--navy)}
.fields{display:flex;gap:10px;margin-top:13px}
.field{height:63px;border:1px solid var(--line);border-radius:14px;padding:12px 14px}
.field small{display:block;font-size:11px;letter-spacing:.1em;color:#6a7280;font-weight:600}
.field span{display:block;font-size:14px;font-weight:500;margin-top:5px}
.search-btn{width:99px;height:63px;border-radius:14px;background:var(--green);font-weight:700;font-size:15px;display:flex;align-items:center;justify-content:center;color:var(--navy-deep)}

/* trip style */
.section-head h2{font-size:50px;line-height:1}
.side-copy{font-size:15px;line-height:25px;color:var(--muted)}
.trip-card{top:1012px;width:508px;height:315px;border-radius:22px;padding:0 26px;overflow:hidden;color:#fff}
.trip-card .orb{position:absolute;top:18px;right:16px;width:132px;height:132px;border-radius:50%;background:rgba(255,255,255,.18)}
.trip-card h3{position:absolute;top:112px;left:26px;font-size:34px;line-height:1.1}
.trip-card p{position:absolute;top:162px;left:26px;width:390px;font-size:14px;line-height:22px}
.trip-card .btn{position:absolute;top:250px;left:26px;height:38px;font-size:14px;color:var(--navy-deep)}
.trip-a{left:81px;background:linear-gradient(160deg,#3f6b34 0%,#24443a 55%,#0f223d 100%)}
.trip-b{left:609px;background:linear-gradient(150deg,#e2a23c 0%,#7b6533 45%,#1b3048 80%,#0f213d 100%)}

/* featured */
.featured{top:1403px;left:0;width:1200px;height:661px;background:var(--sage)}
.chips{top:1624px;left:81px;display:flex;gap:10px}
.chip{height:31px;padding:0 13px;border-radius:999px;background:#fff;border:1px solid var(--line);font-size:13px;font-weight:600;display:flex;align-items:center}
.chip.on{background:#e3efcf;color:var(--green-ink)}
.rv{top:1677px;width:332px;height:311px;background:#fff;border-radius:18px;overflow:hidden;box-shadow:0 6px 18px rgba(20,30,20,.06)}
.rv-img{height:180px;position:relative}
.rv-tag{position:absolute;top:15px;left:14px;height:22px;padding:0 9px;border-radius:999px;background:rgba(255,255,255,.9);font-size:11px;font-weight:600;display:flex;align-items:center;color:var(--ink)}
.rv-tag.green{background:var(--green)}
.rv-heart{position:absolute;top:14px;right:13px;width:34px;height:34px;border-radius:50%;background:#fff;display:flex;align-items:center;justify-content:center}
.rv-body{padding:12px 16px}
.rv-rate{font-size:13px;font-weight:500}
.rv-name{font-size:17px;font-weight:600;margin-top:4px;letter-spacing:-0.01em}
.rv-spec{font-size:12px;color:var(--muted);margin-top:3px}
.rv-foot{display:flex;justify-content:space-between;align-items:baseline;margin-top:12px}
.rv-price{font-size:20px;font-weight:700}
.rv-price small{font-size:19px;font-weight:500;color:var(--muted)}
.rv-note{font-size:13px;color:#475063}

/* owners */
.owners{top:2141px;left:81px;width:1037px;height:495px;border-radius:34px;overflow:hidden;background:
  radial-gradient(circle at 1000px 40px,rgba(60,110,60,.55),transparent 260px),
  linear-gradient(120deg,#10213f 0%,#10223f 55%,#1f4a3d 80%,#3d7a2a 100%)}
.owners h2{position:absolute;top:76px;left:42px;width:490px;font-size:56px;line-height:.98;color:#fff}
.owners .lead{position:absolute;top:264px;left:42px;width:480px;font-size:15px;line-height:25px;color:#e6ebf3}
.owners .lead b{color:#9fd2ff;font-weight:400}
.owners .acts{position:absolute;top:372px;left:42px;display:flex;gap:10px}
.plan{position:absolute;top:43px;left:558px;width:437px;height:411px;background:#fff;border-radius:24px;padding:26px 27px}
.plan .price{font-family:"Inter Tight",sans-serif;font-weight:800;font-size:58px;letter-spacing:-0.05em;margin-top:6px}
.plan .price small{font-family:"Inter",sans-serif;font-size:16px;font-weight:500;letter-spacing:0;color:var(--muted)}
.plan .note{font-size:14px;line-height:24px;color:var(--muted);margin-top:14px}
.row{display:flex;justify-content:space-between;font-size:13px;font-weight:600;padding:14px 0;border-bottom:1px solid var(--line)}
.row:last-of-type{border-bottom:0}
.row .bad{color:#d9534f;text-decoration:line-through}
.row .good{color:var(--green-dark)}
.plan .btn{width:100%;margin-top:10px;height:38px}

/* how */
.how-head{top:2780px;left:0;width:1200px;text-align:center}
.how-head h2{font-size:52px;line-height:1;margin-top:12px}
.how-head p{width:510px;margin:24px auto 0;font-size:15px;line-height:25px;color:var(--muted)}
.step{top:2952px;width:332px;height:220px;background:#fff;border-radius:20px;padding:24px 22px;box-shadow:0 4px 14px rgba(20,30,20,.05)}
.step .num{width:37px;height:37px;border-radius:10px;background:#e4f0d3;color:var(--green-ink);font-size:14px;font-weight:600;display:flex;align-items:center;justify-content:center}
.step h3{font-size:19px;font-weight:600;margin-top:18px;letter-spacing:-0.01em}
.step p{font-size:14px;line-height:22px;color:var(--muted);margin-top:8px}

/* cta */
.cta{top:3267px;left:81px;width:1037px;height:329px;border-radius:34px;text-align:center;color:#fff;background:
  radial-gradient(ellipse at 1000px 320px,rgba(70,130,50,.65),transparent 360px),
  linear-gradient(120deg,#10213f 0%,#13294a 60%,#2a5a35 100%)}
.cta h2{font-size:60px;line-height:.95;width:860px;margin:46px auto 0}
.cta p{width:640px;margin:22px auto 0;font-size:15px;line-height:24px;color:#eef2f7}
.cta .acts{display:flex;justify-content:center;gap:8px;margin-top:18px}

/* footer */
.footer{top:3671px;left:0;width:1200px;height:144px;background:var(--navy-deep);color:#fff}
.footer .brand{position:absolute;top:45px;left:81px;color:#fff;font-size:20px}
.footer .tag{position:absolute;top:84px;left:81px;font-size:13px;color:#cfe3a8}
.footer nav{position:absolute;top:46px;right:82px;display:flex;gap:18px;font-size:14px;font-weight:600;color:#cfe0ff}
</style>
</head>
<body>

<header class="abs hero" role="img" aria-label="Mountain and open road scene at dusk with a setting sun"></header>

<div class="abs nav">
  <div class="brand"><span class="brand-mark"></span>Zandoprik.com</div>
  <nav class="nav-links"><span>Rent an RV</span><span>List your RV</span><span>Flat-rate pricing</span><span>How it works</span></nav>
  <div class="nav-right"><span class="btn btn-white">Owner plan</span><span class="btn btn-green">Start</span></div>
</div>

<div class="abs pill-badge"><i></i>Peer-to-peer RV rentals with owner-first earnings</div>
<h1 class="abs hero-title display">List it. Rent it.<span>Bank it.</span></h1>
<p class="abs hero-copy">Zandoprik.com is a marketplace for travelers to find memorable RV stays and road trips — while owners keep their rental income with one simple monthly membership instead of high per-booking commissions.</p>
<div class="abs hero-cta"><span class="btn btn-green">Find an RV</span><span class="btn btn-ghost">List your RV flat-rate</span></div>
<div class="abs checks" style="top:545px">
  <span class="check"><svg viewBox="0 0 12 12"><path d="M2 6.5l2.5 2.5L10 3" fill="none" stroke="#7cc242" stroke-width="2"/></svg>Pickup or delivery</span>
  <span class="check"><svg viewBox="0 0 12 12"><path d="M2 6.5l2.5 2.5L10 3" fill="none" stroke="#7cc242" stroke-width="2"/></svg>Direct owner payouts</span>
</div>
<div class="abs checks" style="top:591px">
  <span class="check"><svg viewBox="0 0 12 12"><path d="M2 6.5l2.5 2.5L10 3" fill="none" stroke="#7cc242" stroke-width="2"/></svg>No 20%+ platform commission</span>
</div>

<div class="abs hero-art" role="img" aria-label="Illustration of a white camper van on the road"></div>
<div class="abs keep-card"><strong>Keep 100%</strong><p>of the rental price you set after payment processing and your monthly plan.</p></div>

<form class="abs search">
  <div class="tabs"><span class="tab on">RV Rentals</span><span class="tab">Delivered RVs</span><span class="tab">Owner Listings</span></div>
  <div class="fields">
    <div class="field" style="width:283px"><small>LOCATION</small><span>Where are you going?</span></div>
    <div class="field" style="width:208px"><small>DATES</small><span>Any dates</span></div>
    <div class="field" style="width:208px"><small>GUESTS</small><span>2 guests</span></div>
    <div class="field" style="width:168px;position:relative"><small>RENTAL TYPE</small><span>All types</span><svg style="position:absolute;right:14px;top:37px" width="10" height="8" viewBox="0 0 10 8"><path d="M1 2l4 4 4-4" fill="none" stroke="#0e1a2c" stroke-width="1.6"/></svg></div>
    <div class="search-btn">Search</div>
  </div>
</form>

<div class="abs section-head" style="top:915px;left:81px">
  <div class="eyebrow">Choose your trip style</div>
  <h2 class="display" style="margin-top:10px">Adventure made simple.</h2>
</div>
<p class="abs side-copy" style="top:894px;left:618px;width:500px">A simple booking frame inspired by leading RV marketplaces, redesigned for Zandoprik’s darker outdoor look, green accents, and owner-first flat-rate positioning.</p>

<article class="abs trip-card trip-a"><span class="orb"></span><h3 class="display">Get it delivered</h3><p>Have an RV delivered and set up at your campground, festival, tailgate, or private location so your trip starts immediately.</p><span class="btn btn-green">Browse delivered RVs</span></article>
<article class="abs trip-card trip-b"><span class="orb"></span><h3 class="display">Pick it up &amp; hit the road</h3><p>Meet the owner, get a walkthrough, and take the keys for a road trip with flexible pickup near home or your destination.</p><span class="btn btn-green">Browse pickup rentals</span></article>

<section class="abs featured"></section>
<div class="abs section-head" style="top:1480px;left:81px;width:540px">
  <div class="eyebrow">Featured rentals</div>
  <h2 class="display" style="margin-top:10px">Find the right RV for every road.</h2>
</div>
<p class="abs side-copy" style="top:1530px;left:618px;width:500px">Use these cards as a starting framework for inventory listings: image carousel area, rating, location, specs, and nightly pricing.</p>
<div class="abs chips"><span class="chip on">Popular</span><span class="chip">Camper van</span><span class="chip">Pet friendly</span><span class="chip">Budget</span><span class="chip">Luxury</span><span class="chip">Small trailer</span></div>

<article class="abs rv" style="left:81px">
  <div class="rv-img" role="img" aria-label="Class C motorhome photo" style="background:linear-gradient(160deg,#1f3f55,#4c7a4a 60%,#86b24a)">
    <span class="rv-tag">Highly rated</span>
    <span class="rv-heart"><svg width="16" height="14" viewBox="0 0 16 14"><path d="M8 13S1 8.6 1 4.4A3.4 3.4 0 0 1 8 2.8a3.4 3.4 0 0 1 7 1.6C15 8.6 8 13 8 13z" fill="#e0303a"/></svg></span>
  </div>
  <div class="rv-body"><div class="rv-rate">★ 5.0 · 42 reviews</div><div class="rv-name">2024 Pinecrest Sunwander</div><div class="rv-spec">Class C · Sleeps 6 · 28 ft · Asheville, NC</div><div class="rv-foot"><span class="rv-price">$189<small>/night</small></span><span class="rv-note">Delivery available</span></div></div>
</article>
<article class="abs rv" style="left:434px">
  <div class="rv-img" role="img" aria-label="Camper van photo" style="background:linear-gradient(160deg,#1f3450,#8a6236 55%,#e09a3c)">
    <span class="rv-tag">Owner favorite</span>
    <span class="rv-heart"><svg width="16" height="14" viewBox="0 0 16 14"><path d="M8 13S1 8.6 1 4.4A3.4 3.4 0 0 1 8 2.8a3.4 3.4 0 0 1 7 1.6C15 8.6 8 13 8 13z" fill="#e0303a"/></svg></span>
  </div>
  <div class="rv-body"><div class="rv-rate">★ 4.9 · 31 reviews</div><div class="rv-name">Harlowe Vista Adventure Van</div><div class="rv-spec">Camper van · Sleeps 4 · 21 ft · Denver, CO</div><div class="rv-foot"><span class="rv-price">$159<small>/night</small></span><span class="rv-note">Pet friendly</span></div></div>
</article>
<article class="abs rv" style="left:786px">
  <div class="rv-img" role="img" aria-label="Travel trailer photo" style="background:linear-gradient(160deg,#2f5a35,#4c7a5e 50%,#7fa9c9)">
    <span class="rv-tag green">Great value</span>
    <span class="rv-heart"><svg width="16" height="14" viewBox="0 0 16 14"><path d="M8 13S1 8.6 1 4.4A3.4 3.4 0 0 1 8 2.8a3.4 3.4 0 0 1 7 1.6C15 8.6 8 13 8 13z" fill="#e0303a"/></svg></span>
  </div>
  <div class="rv-body"><div class="rv-rate">★ 4.8 · 67 reviews</div><div class="rv-name">Silverline Trailhead Weekend</div><div class="rv-spec">Travel trailer · Sleeps 3 · 20 ft · Austin, TX</div><div class="rv-foot"><span class="rv-price">$119<small>/night</small></span><span class="rv-note">Easy tow</span></div></div>
</article>

<section class="abs owners">
  <div class="eyebrow" style="position:absolute;top:56px;left:42px;color:#9fd66a">For RV owners</div>
  <h2 class="display">One flat monthly rate. You keep the rental earnings.</h2>
  <p class="lead">Other peer-to-peer rental sites often take a percentage from every <b>booking</b>. Zandoprik’s core differentiator is simple: owners pay a predictable monthly membership and keep the rental price they earn.</p>
  <div class="acts"><span class="btn btn-green">List your RV</span><span class="btn btn-white">See how it works</span></div>
  <div class="plan">
    <div class="eyebrow">Owner membership</div>
    <div class="price">$49<small>/month</small></div>
    <p class="note">Example placeholder pricing for the landing-page framework. Update with your final plan.</p>
    <div style="margin-top:10px">
      <div class="row"><span>Zandoprik platform commission</span><span class="good">0%</span></div>
      <div class="row"><span>Typical commission marketplaces</span><span class="bad">20%+</span></div>
      <div class="row"><span>Your pricing control</span><span class="good">Full</span></div>
    </div>
    <span class="btn btn-green">Start earning</span>
  </div>
</section>

<div class="abs how-head">
  <div class="eyebrow">How it works</div>
  <h2 class="display">Built for renters and owners.</h2>
  <p>A one-page foundation covering the main user flow, business model, and conversion points for the Zandoprik marketplace.</p>
</div>
<article class="abs step" style="left:82px"><div class="num">1</div><h3>Search by destination</h3><p>Renters enter location, dates, guests, driver age, and RV type to browse pickup or delivered rentals.</p></article>
<article class="abs step" style="left:434px"><div class="num">2</div><h3>Book with confidence</h3><p>Listings can include owner rules, amenities, verification, insurance messaging, add-ons, delivery, and reviews.</p></article>
<article class="abs step" style="left:786px"><div class="num">3</div><h3>Owners bank more</h3><p>Owners subscribe monthly, control their pricing, manage availability, and keep rental income without high commission fees.</p></article>

<section class="abs cta">
  <h2 class="display">Ready to turn parked time into paid time?</h2>
  <p>Launch the Zandoprik experience with a clear marketplace homepage: search-first for renters, earnings-first for owners, and a brand look pulled from the mountain-road RV artwork.</p>
  <div class="acts"><span class="btn btn-green">Find an RV</span><span class="btn btn-white">List my RV</span></div>
</section>

<footer class="abs footer">
  <div class="brand">Zandoprik.com</div>
  <div class="tag">List it · Rent it · Bank it</div>
  <nav><span>Rent</span><span>Owners</span><span>How it works</span><span>Search</span></nav>
</footer>

</body>
</html>
```